church business card design

we have a logo and would like our business card to complement the logo. we would prefer the logo in white on a coloured background - probably blue. Under the logo or near it we would have the Words 'Love God. Love people. Follow Jesus.'
We would like some yellow/gold highlights. We like the design by marlow inkworks 88 front of card - https://www.pitchvelta.com/businesscard-design/contest/5182094

Our church is multicultural, inner city, friendly, warm welcoming and that's the feel we would like. there's also an element of being spontaneous, so a swirl or swoosh might help give that feel. the example card above had some curved shapes on the front of the card for example.
on the second side of the card would have the details of the Senior Pastor and the contact details for the church.
after the business card we would be looking at letterhead and an A5 flyer for printing but also as document templates so we can create invitations etc going forward

```html
<!DOCTYPE html>
<html lang="en">
<head>
<meta charset="UTF-8">
<title>Harbour Stone Church – Business Card</title>
<link href="https://fonts.googleapis.com/css2?family=Montserrat:wght@700;800&family=Roboto:wght@400;500&display=swap" rel="stylesheet">
<style>
  :root {
    --page-bg: #e4e4e6;
    --card-blue: #243d8f;
    --card-blue-deep: #213886;
    --ink-white: #ffffff;
    --shadow: rgba(0, 0, 0, 0.28);
  }
  * { box-sizing: border-box; margin: 0; padding: 0; }
  html, body {
    width: 1200px;
    height: 900px;
    overflow: hidden;
    background: var(--page-bg);
  }
  .stage {
    width: 1200px;
    height: 900px;
    display: flex;
    flex-direction: column;
    align-items: center;
    justify-content: center;
    gap: 36px;
  }
  .card {
    position: relative;
    width: 700px;
    height: 400px;
    border-radius: 26px;
    background: var(--card-blue);
    color: var(--ink-white);
    box-shadow: 0 6px 14px var(--shadow);
    overflow: hidden;
    font-family: "Roboto", Arial, sans-serif;
  }
  .card-front {
    display: flex;
    flex-direction: column;
    align-items: center;
    justify-content: center;
    gap: 40px;
  }
  .church-name {
    display: flex;
    align-items: center;
    gap: 14px;
    font-family: "Montserrat", Arial, sans-serif;
    font-weight: 800;
    color: var(--ink-white);
    letter-spacing: 0.5px;
    line-height: 1.05;
  }
  .church-name .name-dot {
    flex: none;
    border-radius: 50%;
    background: var(--ink-white);
  }
  .card-front .church-name { font-size: 40px; }
  .card-front .church-name .name-dot { width: 22px; height: 22px; }
  .tagline {
    font-size: 19px;
    letter-spacing: 0.6px;
  }
  .tagline .divider { margin: 0 10px; }

  .card-back .church-name {
    position: absolute;
    left: 48px;
    top: 58px;
    font-size: 30px;
    max-width: 320px;
  }
  .card-back .church-name .name-dot { width: 18px; height: 18px; }
  .person {
    position: absolute;
    left: 48px;
    top: 190px;
  }
  .person-name {
    font-family: "Montserrat", Arial, sans-serif;
    font-weight: 800;
    font-size: 30px;
    letter-spacing: 0.5px;
  }
  .person-role {
    font-size: 18px;
    margin-top: 2px;
  }
  .contact-list {
    list-style: none;
    position: absolute;
    left: 48px;
    top: 282px;
    font-size: 17px;
    line-height: 27px;
  }
  .contact-list li { display: flex; align-items: center; gap: 10px; }
  .contact-list svg { width: 14px; height: 14px; fill: var(--ink-white); flex: none; }
  .address {
    position: absolute;
    right: 44px;
    top: 180px;
    text-align: right;
    font-size: 17px;
    line-height: 24px;
  }
</style>
</head>
<body>
<main class="stage">
  <section class="card card-front" aria-label="Card front">
    <div class="church-name"><span class="name-dot"></span>Harbour Stone Church</div>
    <p class="tagline">Love God<span class="divider">|</span>Love people<span class="divider">|</span>Follow Jesus</p>
  </section>

  <section class="card card-back" aria-label="Card back">
    <div class="church-name"><span class="name-dot"></span>Harbour Stone Church</div>
    <div class="person">
      <h1 class="person-name">DANIEL HART</h1>
      <p class="person-role">CEO/Founder</p>
    </div>
    <ul class="contact-list">
      <li>
        <svg viewBox="0 0 24 24" aria-hidden="true"><path d="M6.6 10.8a15.1 15.1 0 0 0 6.6 6.6l2.2-2.2a1 1 0 0 1 1-.25 11.4 11.4 0 0 0 3.6.57 1 1 0 0 1 1 1V20a1 1 0 0 1-1 1A17 17 0 0 1 3 4a1 1 0 0 1 1-1h3.5a1 1 0 0 1 1 1c0 1.25.2 2.45.57 3.57a1 1 0 0 1-.25 1z"/></svg>
        (555) 210 3398
      </li>
      <li>
        <svg viewBox="0 0 24 24" aria-hidden="true"><path d="M2 5h20v14H2z M3.5 6.5 12 13l8.5-6.5" fill="var(--ink-white)" stroke="var(--card-blue)" stroke-width="1.6"/></svg>
        hello@harbourstone.org
      </li>
      <li>
        <svg viewBox="0 0 24 24" aria-hidden="true"><circle cx="12" cy="12" r="10"/><path d="M2 12h20M12 2c3 3 3 17 0 20M12 2c-3 3-3 17 0 20" fill="none" stroke="var(--card-blue)" stroke-width="1.5"/></svg>
        www.harbourstone.org
      </li>
    </ul>
    <p class="address">Suite 8, 61 Wharf Lane<br>Eastbridge QLD 4102</p>
  </section>
</main>
</body>
</html>
```